Webdesign für Metallbau-Wasserkraft Tessmar Lauber GmbH & Co. KG
Zielgruppe
Das Unternehmen ist im Metall- und Stahlwasserbau tätig. Die Haupkompetenz liegt im Stahlwasserbau, Rechenreinigung und Stahlbau tätig.
Aufgabenstellung
Die vorhandenen Seite https://www.metallbau-tessmar-lauber-beispiel.de/ soll einen Relaunch erhalten. Das Design soll frisch, modern und aussagekräftig erscheinen, trotz der Tradition und des Handwerksbetriebes.
Die Navigationstruktur soll erhalten bleiben. Hinzu kommt der Punkt 'Neuigkeiten'.

```html
<!DOCTYPE html>
<html lang="de">
<head>
<meta charset="utf-8">
<title>Metallbau-Wasserkraft Tessmar Lauber GmbH &amp; Co. KG</title>
<link href="https://fonts.googleapis.com/css2?family=Manrope:wght@300;400;500;600&family=Inter:wght@400;500&display=swap" rel="stylesheet">
<style>
:root{
  --blue:#1b7fb8;
  --ink:#1a1a1a;
  --line:#d6d6d6;
  --panel:#dcdcdc;
  --white:#fff;
}
*{box-sizing:border-box;margin:0;padding:0}
html,body{width:1200px;height:4283px;overflow:hidden}
body{position:relative;background:var(--white);font-family:"Manrope",sans-serif;color:var(--ink)}
.abs{position:absolute}
.small{font-family:"Inter",sans-serif}
.eyebrow{position:absolute;font-family:"Inter",sans-serif;font-size:14px;color:var(--blue);letter-spacing:.3px}

.hero{left:0;top:0;width:1200px;height:652px;background:linear-gradient(180deg,#7f96ad 0%,#b9c9d8 18%,#5f7a55 42%,#3f5a44 52%,#9fb0b8 62%,#7d8f96 80%,#56666c 100%)}
.topbar{left:0;top:0;width:1200px;height:55px;background:linear-gradient(90deg,rgba(60,70,80,.55),rgba(120,130,140,.35))}
.brand{left:26px;top:14px;display:flex;align-items:center;gap:12px;color:#fff;font-size:9px;font-weight:500;letter-spacing:1px;line-height:12px;text-transform:uppercase}
.brand .mark{width:26px;height:26px;border:2px solid currentColor}
.nav{right:26px;top:20px;display:flex;gap:17px;font-family:"Inter",sans-serif;font-size:13px;color:#fff}
.hero-title{left:55px;top:210px;width:700px;font-size:50px;font-weight:300;line-height:58px;color:#fff;letter-spacing:-.5px}
.btn{display:flex;align-items:center;justify-content:center;gap:10px;background:var(--blue);color:#fff;border-radius:22px;font-family:"Inter",sans-serif;font-size:13px}
.hero-btn{left:55px;top:356px;width:125px;height:38px}
.glass{left:55px;top:464px;width:1089px;height:143px;border-radius:14px;background:rgba(255,255,255,.22);backdrop-filter:blur(6px)}
.glass .name{position:absolute;left:27px;top:24px;font-size:34px;font-weight:300;line-height:52px;color:#fff}
.glass .claim{position:absolute;left:565px;top:36px;font-size:24px;font-weight:300;line-height:37px;color:#fff;letter-spacing:-.3px}

.intro{left:55px;top:890px;width:480px;font-size:30px;line-height:38px;font-weight:400;letter-spacing:-.4px}
.stat{left:628px;width:516px;height:150px;border-bottom:1px solid var(--line);display:flex;align-items:flex-end;padding-bottom:24px}
.stat b{font-weight:300;font-size:84px;line-height:1;color:var(--blue);letter-spacing:-2px}
.stat span{font-family:"Inter",sans-serif;font-size:14px;margin:0 0 10px 10px}

.h2{font-size:36px;font-weight:400;letter-spacing:-.4px}
.card{top:1469px;width:353px;height:638px;border:1px solid var(--line);border-radius:14px}
.card .photo{position:absolute;left:17px;top:14px;width:319px;height:319px;border-radius:14px}
.card h3{position:absolute;left:0;width:100%;top:370px;text-align:center;font-size:33px;font-weight:300;color:var(--blue)}
.card ul{position:absolute;left:0;width:100%;top:420px;list-style:none;text-align:center;font-family:"Inter",sans-serif;font-size:17px;line-height:29.4px}

.team-photo{left:35px;top:2323px;width:517px;height:519px;border-radius:14px;background:linear-gradient(180deg,#9aa6a8 0%,#c9cfcf 25%,#6d7779 55%,#39434b 100%)}
.body-text{left:608px;top:2388px;width:505px;font-size:24px;line-height:36.5px;font-weight:400;letter-spacing:-.5px}

.form-panel{left:627px;top:3053px;width:517px;height:492px;background:var(--panel);border-radius:16px}
.label{position:absolute;font-family:"Inter",sans-serif;font-size:15px;font-weight:500}
.field{position:absolute;background:#fff;border:1px solid #c8c8c8;border-radius:8px}

.footer{left:0;top:3640px;width:1200px;height:643px;background:linear-gradient(180deg,#fff 0%,#cfe3ef 25%,#7cb3d4 60%,#2d8cc2 100%)}
.flinks{left:63px;top:3900px;list-style:none;font-size:25px;font-weight:600;line-height:42.5px;letter-spacing:-.5px}
.faddr{left:633px;font-size:16px;letter-spacing:-.3px}
</style>
</head>
<body>

<section class="abs hero" role="img" aria-label="Stausee mit bewaldeten Hügeln und Entnahmeturm aus Beton"></section>
<header class="abs topbar"></header>
<div class="abs brand"><span class="mark"></span><span>Metallbau-Wasserkraft<br>Tessmar Lauber GmbH &amp; Co.KG</span></div>
<nav class="abs nav"><span>Über uns</span><span>Stahlwasserbau</span><span>Rechenreiniger</span><span>Weitere Stahlbau-Produkte</span><span>Neuigkeiten</span></nav>
<h1 class="abs hero-title">Stahlwasserbau mit Tradition und Innovation</h1>
<div class="abs btn hero-btn">Über uns
  <svg width="12" height="12" viewBox="0 0 12 12"><path d="M2 6h8M6.5 2.5 10 6l-3.5 3.5" stroke="#fff" stroke-width="1.4" fill="none"/></svg></div>
<div class="abs glass">
  <div class="name">Metallbau Wasserkraft<br>Tessmar Lauber</div>
  <div class="claim">Ihr Partner im Metallbau und Stahlwasserbau<br>in Steinbrück bei Waldhain</div>
</div>

<div class="eyebrow" style="left:55px;top:864px">IN ZAHLEN</div>
<p class="abs intro">Metallbau Wasserkraft Tessmar Lauber – ein Name, der in ganz Deutschland für qualitativ hochwertigen Stahlwasser- und Metallbau, fachgerechte Montage und umfassenden Kundenservice steht.</p>
<div class="abs stat" style="top:701px"><b>45</b><span>Jahre Erfahrung</span></div>
<div class="abs stat" style="top:852px"><b>50 +</b><span>Länder mit unseren Produkten</span></div>
<div class="abs stat" style="top:1003px"><b>30%</b><span>Auftragswachstum / Jahr</span></div>

<h2 class="abs h2" style="left:55px;top:1330px">Unsere Produkte und Leistungen</h2>
<div class="eyebrow" style="right:56px;top:1333px">LEISTUNGEN</div>
<p class="abs" style="left:55px;top:1401px;font-size:23px;letter-spacing:-.5px">Folgende Produkte können wir als versierter Fachbetrieb für Sie fertigen:</p>

<article class="abs card" style="left:55px">
  <div class="photo" role="img" aria-label="Wehranlage an einem Fluss mit Strommast" style="background:linear-gradient(180deg,#cfd6da 0%,#b9c2c3 45%,#7f8a86 70%,#a8b0ad 100%)"></div>
  <h3>Stahlwasserbau</h3>
  <ul style="top:424px"><li>Schützanlagen</li><li>Dammtafeln</li><li>Wehrklappen</li><li>Fischaufstiegshilfen</li><li>Rechenanlagen</li><li>Schwimmbalken</li><li>Hochwasserschutztore</li></ul>
</article>
<article class="abs card" style="left:424px">
  <div class="photo" role="img" aria-label="Wasser fließt über gestufte Wehrkanten" style="background:linear-gradient(180deg,#9c8f80 0%,#d7d4cf 35%,#7a5f45 60%,#c9c6c0 100%);top:18px"></div>
  <h3 style="top:374px">Rechenreiniger</h3>
  <ul style="top:428px"><li>Stangenreiniger</li><li>Horizontal-Rechenreiniger</li><li>Knickarmreiniger</li></ul>
</article>
<article class="abs card" style="left:791px">
  <div class="photo" role="img" aria-label="Stahlkonstruktion in Schwarz-Weiß von unten" style="background:linear-gradient(135deg,#2f2f2f 0%,#8c8c8c 40%,#d8d8d8 60%,#4a4a4a 100%);top:18px"></div>
  <h3 style="top:374px">Stahlbau</h3>
  <ul style="top:428px"><li>Treppen &amp; Stege</li><li>Geländer</li></ul>
</article>

<div class="eyebrow" style="left:35px;top:2274px">INNOVATION</div>
<div class="abs team-photo" role="img" aria-label="Zwei Fachleute prüfen einen Plan vor einer Wehranlage"></div>
<h2 class="abs" style="left:608px;top:2322px;font-size:32px;font-weight:400;letter-spacing:-.4px">Was uns bewegt</h2>
<p class="abs body-text">Die Zufriedenheit unserer Kunden treibt uns an. Um das Niveau unserer Fertigungsqualität auch in den kommenden Jahren stetig zu steigern, nutzen wir vielfältige Weiter- und Fortbildungsangebote.<br>Die intensive und enge Zusammenarbeit mit unseren Kunden nutzen wir, um Markttendenzen früh zu erkennen und neue Wege zu gehen.</p>

<div class="eyebrow" style="left:53px;top:3058px">KONTAKT</div>
<p class="abs" style="left:53px;top:3112px;width:500px;font-size:24px;line-height:36.5px;letter-spacing:-.6px">&nbsp;Natürlich wissen wir um die Vorteile persönlicher Beratung und legen Wert auf eine individuelle Kundenbetreuung.</p>
<p class="abs" style="left:53px;top:3250px;width:540px;font-size:36px;line-height:52px;letter-spacing:-.6px">Schreiben Sie uns eine Nachricht - unser Team freut sich über Ihre Anfrage!</p>

<form class="abs form-panel">
  <span class="label" style="left:34px;top:38px">Name</span>
  <span class="label" style="left:269px;top:38px">Email</span>
  <span class="field" style="left:34px;top:68px;width:212px;height:59px"></span>
  <span class="field" style="left:269px;top:68px;width:213px;height:59px"></span>
  <span class="label" style="left:34px;top:156px">Unternehmen</span>
  <span class="field" style="left:34px;top:188px;width:448px;height:58px"></span>
  <span class="label" style="left:34px;top:274px">Nachricht</span>
  <span class="field" style="left:34px;top:306px;width:448px;height:81px"></span>
  <span class="abs btn" style="left:34px;top:409px;width:172px;height:45px;font-size:14px">Nachricht senden</span>
</form>

<footer class="abs footer"></footer>
<div class="abs brand" style="left:63px;top:3746px;color:#1a4f78;font-size:11px;line-height:15px;font-weight:600"><span class="mark" style="width:30px;height:30px"></span><span>Metallbau-Wasserkraft<br>Tessmar Lauber GmbH &amp; Co.KG</span></div>
<p class="abs" style="left:620px;top:3744px;font-size:24px;letter-spacing:-.6px">Stahlwasserbau mit Tradition und Innovation.</p>
<ul class="abs flinks"><li>Über uns</li><li>Kontakt</li><li>Impressum</li><li>Datenschutz</li><li>Sitemap</li></ul>
<p class="abs" style="left:633px;top:3918px;font-size:24px;line-height:37px;letter-spacing:-.6px">Metallbau-Wasserkraft Tessmar Lauber<br>GmbH &amp; Co. KG</p>
<p class="abs faddr" style="top:3997px">Lindenhangweg 14, 08147 Steinbrück</p>
<p class="abs faddr" style="top:4040px;line-height:26px">Telefon: 034512 55810<br>Telefax: 034512 55811</p>
<p class="abs faddr" style="top:4114px">Mail: info@metallbau-tessmar-lauber-beispiel.de</p>
<p class="abs small" style="left:63px;top:4216px;font-size:13px">© 2024 All rights reserved</p>

</body>
</html>
```